Label design for olive oil and other oils

We are a company located in Melbourne, doing the international trade, now we are starting a olive oil project and need a label for our product. Our olive oil named "Blue Heron", our products is produce in Australia and will export oversea, The label should be brief and clear. We offer the natural and premium products to our customers. The bottles of the oil will be 500ml, 750ml and 1L. Our label will use for other kinds of oil in the future, such as the nut oil, almond oil and macadamia oil, so we would like the design can be expand to other oil as well, so a series of oil label will be welcomed.

Target Market(s)

Australia local market and oversea.

Industry/Entity Type

Food Store

Requirements
Must have
• none
Nice to have
• The blue heron bird
Should not have
• none

```html
<!DOCTYPE html>
<html lang="en">
<head>
<meta charset="utf-8">
<title>Blue Heron Natural Organic Olive Oil – Label</title>
<link rel="stylesheet" href="https://fonts.googleapis.com/css2?family=Courier+Prime:wght@700&display=swap">
<style>
  :root {
    --page: #ffffff;
    --label-cream: #f6f1d8;
    --frame: #d2ccab;
    --frame-dark: #a9a37e;
    --brand-brown: #6e4a28;
    --olive-band: #5d5b2b;
    --olive-band-text: #f6f1d8;
    --leaf-green: #8fa83c;
    --leaf-light: #c4d46a;
    --ink-soft: #7a6a4a;
  }
  * { margin: 0; padding: 0; box-sizing: border-box; }
  html, body {
    width: 783px; height: 1200px; overflow: hidden;
    background: var(--page);
  }
  .canvas { position: relative; width: 783px; height: 1200px; }

  .label {
    position: absolute; left: 224px; top: 30px;
    width: 335px; height: 1140px;
    background: var(--label-cream);
    border: 6px solid var(--frame);
    border-radius: 40px;
    text-align: center;
    color: var(--brand-brown);
    font-family: "Courier Prime", "Courier New", monospace;
    font-weight: 700;
  }
  .label::after {
    content: ""; position: absolute; inset: 10px;
    border: 2px solid var(--frame);
    border-radius: 30px;
    pointer-events: none;
  }

  .brand-dot {
    position: absolute; left: 50%; top: 62px;
    width: 56px; height: 56px; transform: translateX(-50%);
    background: var(--brand-brown);
    border-radius: 50%;
  }

  .brand {
    position: absolute; left: 0; right: 0; top: 148px;
    font-size: 66px; line-height: 80px; font-weight: 700;
    color: var(--brand-brown);
  }

  .origin {
    position: absolute; left: 40px; right: 40px; top: 336px;
    font-size: 16px; line-height: 26px;
    border-bottom: 2px solid var(--frame-dark);
  }

  .claim {
    position: absolute; left: 0; right: 0; top: 384px;
    font-size: 44px; line-height: 52px;
  }

  .variety {
    position: absolute; left: 40px; right: 40px; top: 500px; height: 58px;
    background: var(--olive-band);
    border-radius: 4px;
    font-size: 36px; line-height: 58px; color: var(--olive-band-text);
  }

  .olive-branch {
    position: absolute; left: 50%; top: 610px;
    width: 220px; height: 380px; transform: translateX(-50%);
    border-radius: 50%;
    background: radial-gradient(ellipse at 50% 45%, var(--leaf-light) 0%, var(--leaf-green) 75%, rgba(143,168,60,0.0) 100%);
  }

  .divider {
    position: absolute; left: 40px; right: 40px; top: 1030px;
    border-top: 2px dashed var(--frame-dark);
  }

  .volume {
    position: absolute; left: 0; right: 0; top: 1046px;
    font-size: 26px; line-height: 34px; color: var(--ink-soft);
  }

  .footer-rule {
    position: absolute; left: 40px; right: 40px; top: 1092px;
    border-top: 2px dashed var(--frame-dark);
  }
</style>
</head>
<body>
<main class="canvas">
  <section class="label">
    <div class="brand-dot"></div>

    <h1 class="brand">Blue<br>Heron</h1>

    <p class="origin">Products Of Australia</p>

    <p class="claim">Natural<br>Organic</p>

    <p class="variety">Olive Oil</p>

    <div class="olive-branch" role="img" aria-label="Illustration of a green olive branch with olives and leaves"></div>

    <div class="divider"></div>
    <p class="volume">750ml</p>
    <div class="footer-rule"></div>
  </section>
</main>
</body>
</html>
```